Website Design Brief for KBR LEGAL PTY LTD

Company Name: KBR LEGAL PTY LTD

Industry: Legal Services

Target Audience:

Corporate clients
Business owners
Individuals seeking legal advice in Commercial Law, Mergers and Acquisitions, Will Law, Property Law, and Conveyancing
Objective:

To create a professional, user-friendly website that establishes trust and authority in the legal field.
Provide easy access to information about the firm’s services, team, and areas of expertise.
Include client testimonials, contact information, and a blog or resource section for legal insights.
Key Features and Pages:

Homepage:

Clean, modern design with a professional feel.
Introduction to KBR LEGAL with a brief overview of services.
High-quality images or illustrations related to law and professionalism.
Prominent call-to-action (CTA) like "Get in Touch" or "Book a Consultation."
About Us:

Information about the firm's mission, values, and team.
Highlight the expertise and experience of key members.
Include a brief company history, if relevant.
Services:

Detailed descriptions of services, categorized by legal areas (e.g., Commercial Law, Mergers & Acquisitions, Property Law, etc.).
Call-to-action buttons to encourage potential clients to reach out for consultations.
Team:

Profiles of key team members, including their qualifications, expertise, and professional photos.
Include links to their professional networks (LinkedIn).
Testimonials:

Section showcasing positive client testimonials or case studies.
This can help build trust and credibility with potential clients.
Blog or Resources:

A blog or resources section providing legal tips, industry news, and insights.
Content should demonstrate the firm’s knowledge and thought leadership.
Contact Us:

Easy-to-use contact form.
Include phone number, email, physical office address, and possibly a map.
Option for booking consultations or initial meetings directly online.
Client Portal (optional):

Secure login for clients to access their case information, documents, and updates (this could be an advanced feature to consider after launch).
Design Aesthetic:

Clean, modern, and professional.
Elegant use of fonts and a color palette that reflects trust, authority, and sophistication (dark blues, whites, grays).
User-friendly navigation to ensure clients can easily find the information they need.
Technical Considerations:

The website should be mobile-responsive and look great on all devices (desktop, tablet, mobile).
Ensure fast load times and optimized images.
Implement SEO best practices to improve search engine rankings.
Easy-to-update CMS (WordPress or similar) to allow easy future updates.
Competitor/Inspirational Websites:

[Provide examples of legal firms' websites you like, or any designs that reflect the feel you want for your firm.]
Additional Information:

Please ensure all content is aligned with the firm's professional tone and approach.
The website should be designed to be scalable for future growth (adding more services, resources, etc.).

Target Market(s)

Business owners Individuals seeking legal advice in Commercial Law, Mergers and Acquisitions, Will Law, Property Law, and Conveyancing

Industry/Entity Type

Legal

Number of Pages Required

3 page

Requirements
Must have
• Home Page, About Us, Contact Us, Services

```html
<!DOCTYPE html>
<html lang="en">
<head>
<meta charset="utf-8">
<title>KBR LEGAL – Your Trusted Legal Partner</title>
<link href="https://fonts.googleapis.com/css2?family=Montserrat:wght@300;400;500;600;700&family=Poppins:ital,wght@0,300;0,400;0,500;0,600;1,400&display=swap" rel="stylesheet">
<style>
:root{
  --navy:#17467c;
  --navy-deep:#1b3d66;
  --band:#255587;
  --footer:#1f4b7d;
  --ink:#1c2a3a;
  --muted:#5d6673;
  --line:#c9d3df;
  --white:#ffffff;
  --map:#e7ebef;
}
*{box-sizing:border-box;margin:0;padding:0}
html,body{width:1200px;height:4147px;overflow:hidden}
body{font-family:"Poppins",sans-serif;color:var(--ink);background:var(--white);position:relative}
h1,h2,h3,h4,.brand{font-family:"Montserrat",sans-serif}
a{color:inherit;text-decoration:none}
section,header,footer{position:absolute;left:0;width:1200px}
.abs{position:absolute}

/* hero */
.hero{top:0;height:676px;background:linear-gradient(120deg,#2c4a74 0%,#1e3e6a 45%,#274c7b 100%);color:var(--white)}
.hero-photo{position:absolute;inset:0;background:radial-gradient(ellipse at 25% 45%,rgba(120,140,170,.35),transparent 60%),radial-gradient(ellipse at 80% 70%,rgba(90,110,140,.3),transparent 55%)}
.brand{font-size:30px;font-weight:600;letter-spacing:.5px;color:var(--white)}
.nav{position:absolute;top:28px;left:360px;display:flex;gap:25px;font-size:13px}
.btn-touch{position:absolute;left:990px;top:19px;width:150px;height:39px;background:var(--white);color:var(--navy);font-weight:600;font-size:14px;display:flex;align-items:center;justify-content:center;border-radius:2px}
.hero h1{position:absolute;top:258px;width:100%;text-align:center;font-size:42px;line-height:50px;font-weight:600}
.hero h1 span{display:block;font-weight:300}
.hero .lead{position:absolute;top:372px;width:100%;text-align:center;font-size:15px;line-height:22px}
.btn-light{position:absolute;left:488px;top:433px;width:224px;height:40px;background:var(--white);color:var(--navy);font-weight:500;font-size:14px;display:flex;align-items:center;justify-content:center;border-radius:2px}

/* about */
.about{top:676px;height:510px}
.photo{background:linear-gradient(150deg,#c9ced6,#8d97a5 60%,#5d6878)}
.eyebrow{font-size:18px;color:var(--navy)}
.about h2{font-size:33px;font-weight:700;color:var(--navy)}
.about p{font-size:12.5px;line-height:21px;color:var(--muted)}
.btn{display:flex;align-items:center;justify-content:center;background:var(--navy);color:var(--white);font-weight:500;font-size:14px;border-radius:2px}

/* services */
.services{top:1186px;height:525px;background:linear-gradient(135deg,#2a5a8c,#1f4e80 60%,#2b5b8c);color:var(--white)}
.services h2{font-size:33px;font-weight:600}
.services .intro{font-size:12.5px;line-height:22px}
.card{position:absolute;width:351px;height:174px;border:1px solid rgba(255,255,255,.75);border-radius:3px}
.card .icon{position:absolute;left:24px;top:30px;width:66px;height:66px;background:var(--white);border-radius:3px;display:flex;align-items:center;justify-content:center}
.card h3{position:absolute;left:128px;top:28px;font-size:17px;font-weight:600}
.card p{position:absolute;left:128px;top:56px;width:205px;font-size:12px;line-height:20px;color:#dce6f1}
.card .more{position:absolute;left:128px;top:124px;font-size:12px;font-style:italic;text-decoration:underline;color:#dce6f1}

/* team */
.team{top:1711px;height:580px}
.center{width:100%;text-align:center}
.section-title{font-size:34px;font-weight:700;color:var(--navy)}
.member-photo{position:absolute;top:162px;width:345px;height:315px}
.name-box{position:absolute;top:434px;width:265px;height:73px;background:var(--white);box-shadow:0 4px 14px rgba(0,0,0,.12);padding:15px 0 0 18px}
.name-box h4{font-size:17px;font-weight:600;color:var(--navy-deep)}
.name-box span{font-size:11px;color:var(--ink)}
.name-box .social{position:absolute;right:20px;top:20px;width:34px;height:34px;background:var(--navy)}

/* testimonials */
.testimonials{top:2291px;height:451px;background:linear-gradient(135deg,#285889,#1e4c7e);color:var(--white)}
.testimonials h2{font-size:32px;font-weight:500}
.testimonials blockquote{position:absolute;left:255px;top:182px;width:690px;text-align:center;font-style:italic;font-size:15px;line-height:24px}
.dots{position:absolute;top:399px;left:578px;display:flex;gap:4px}
.dots i{width:7px;height:7px;border:1px solid var(--white);display:block}
.dots i.on{background:var(--white)}

/* blog */
.blog{top:2742px;height:585px}
.post{position:absolute;top:164px;width:345px;height:344px;box-shadow:0 3px 12px rgba(0,0,0,.08);background:var(--white)}
.post .thumb{height:172px;background:linear-gradient(160deg,#aab3bf,#6b7788 60%,#43506a)}
.post .date{position:absolute;right:0;top:0;width:50px;height:48px;background:var(--navy);color:var(--white);font-size:11px;line-height:14px;text-align:center;padding-top:8px}
.post h4{margin:20px 0 0 13px;font-size:15px;font-weight:600;color:var(--navy)}
.post p{margin:8px 13px 0;font-size:12.5px;line-height:21px;color:var(--muted)}
.post .btn{position:absolute;left:12px;top:289px;width:120px;height:33px}

/* contact */
.contact{top:3327px;height:488px;background:var(--map)}
.map{position:absolute;inset:0;background:linear-gradient(135deg,#eef1f3,#dfe5ea 60%,#e9ede9)}
.contact-panel{position:absolute;left:60px;top:22px;width:525px;height:466px;background:var(--white)}
.contact-panel h2{position:absolute;left:42px;top:40px;font-size:34px;font-weight:600;color:var(--navy)}
.info{position:absolute;left:42px;display:flex;gap:12px;align-items:center;font-size:13px;color:var(--navy-deep)}
.field{position:absolute;border-bottom:1px solid #7f8ea0;font-size:13px;color:#333;padding-bottom:14px}

/* footer */
.footer{top:3815px;height:332px;background:var(--footer);color:var(--white)}
.footer h4{font-size:16px;font-weight:600;margin-bottom:12px}
.footer ul{list-style:none;font-size:12.5px;line-height:26px}
.circle{width:38px;height:38px;border:1.5px solid var(--white);border-radius:50%}
</style>
</head>
<body>

<header class="hero">
  <div class="hero-photo" role="img" aria-label="Lawyer's desk with laptop and scales of justice statue, tinted dark blue"></div>
  <div class="brand abs" style="left:60px;top:18px">KBR LEGAL</div>
  <nav class="nav">
    <a href="#">Home</a><a href="#">About Us</a><a href="#">Services</a><a href="#">Team</a><a href="#">Testimonials</a><a href="#">Blog</a><a href="#">Contact Us</a><a href="#">Client Portal</a>
  </nav>
  <a class="btn-touch" href="#">Get in Touch</a>
  <h1>YOUR TRUSTED LEGAL PARTNER IN<span>BUSINESS AND BEYOND</span></h1>
  <p class="lead">Expert Legal Services Tailored to Your Needs in Commercial Law,<br>Mergers &amp; Acquisitions, Property Law, and More</p>
  <a class="btn-light" href="#">BOOK A CONSULTATION</a>
</header>

<section class="about">
  <div class="photo abs" style="left:93px;top:69px;width:227px;height:335px" role="img" aria-label="Lawyer reviewing a document with a client"></div>
  <div class="photo abs" style="left:330px;top:100px;width:226px;height:334px" role="img" aria-label="Lawyer working at a desk in an office"></div>
  <div class="abs" style="left:618px;top:74px;width:520px">
    <div class="eyebrow">About</div>
    <h2 style="margin-top:2px">KBR LEGAL</h2>
    <p style="margin-top:12px">At KBR LEGAL, we are committed to providing comprehensive and reliable legal services to businesses and individuals. With years of expertise in commercial law, property law, mergers and acquisitions, and will law, we help our clients navigate complex legal landscapes with confidence.</p>
    <p style="margin-top:13px">At KBR LEGAL, we are committed to providing comprehensive and reliable legal services to businesses and individuals. With years of expertise in commercial law, property law, mergers and acquisitions, and will law, we help our clients navigate complex legal landscapes with confidence.</p>
  </div>
  <a class="btn abs" href="#" style="left:617px;top:356px;width:127px;height:39px">Learn More</a>
</section>

<section class="services">
  <h2 class="abs" style="left:60px;top:70px">SERVICE</h2>
  <p class="intro abs" style="left:60px;top:116px;width:300px">Lorem Ipsum has been the industry's standard dummy text ever since the 1500s, when an unknown printer. Ipsum has been the industry's standard dummy text ever since the 1500.</p>

  <div class="card" style="left:425px;top:65px">
    <div class="icon"><svg width="40" height="40" viewBox="0 0 40 40" fill="none" stroke="#17467c" stroke-width="1.6"><rect x="6" y="16" width="12" height="20"/><rect x="20" y="8" width="14" height="28"/><path d="M9 21h6M9 26h6M9 31h6M24 13h6M24 19h6M24 25h6M24 31h6"/></svg></div>
    <h3>COMMERCIAL LAW</h3>
    <p>Protecting Your Business Interests Business Interests</p>
    <a class="more" href="#">Learn More</a>
  </div>
  <div class="card" style="left:790px;top:65px">
    <div class="icon"><svg width="40" height="40" viewBox="0 0 40 40" fill="none" stroke="#17467c" stroke-width="1.6"><rect x="7" y="4" width="24" height="30"/><path d="M19 9v12M12 12h14M12 12l-3 6h6zM26 12l-3 6h6z"/><path d="M14 30l6-4 6 4"/></svg></div>
    <h3>ACQUISITIONS LAW</h3>
    <p>Guiding You Through Complex Transactions Complex Transactions</p>
    <a class="more" href="#">Learn More</a>
  </div>
  <div class="card" style="left:60px;top:271px">
    <div class="icon"><svg width="40" height="40" viewBox="0 0 40 40" fill="none" stroke="#17467c" stroke-width="1.6"><path d="M5 20L20 6l15 14M9 17v17h22V17"/><path d="M15 27l5-5 5 5M20 22v9"/></svg></div>
    <h3>PROPERTY LAW</h3>
    <p>Helping You Navigate Property Transactions Helping You Transactions</p>
    <a class="more" href="#">Learn More</a>
  </div>
  <div class="card" style="left:425px;top:271px">
    <div class="icon"><svg width="40" height="40" viewBox="0 0 40 40" fill="none" stroke="#17467c" stroke-width="1.6"><rect x="8" y="5" width="22" height="30"/><path d="M12 12h14M12 17h14M12 22h9"/><circle cx="26" cy="28" r="4"/></svg></div>
    <h3>WILLSLAW</h3>
    <p>Safeguarding Your Legacy Safeguarding Your Legacy</p>
    <a class="more" href="#">Learn More</a>
  </div>
  <div class="card" style="left:790px;top:271px">
    <div class="icon"><svg width="40" height="40" viewBox="0 0 40 40" fill="none" stroke="#17467c" stroke-width="1.6"><rect x="7" y="4" width="24" height="30"/><path d="M19 9v12M12 12h14M12 12l-3 6h6zM26 12l-3 6h6z"/><path d="M14 30l6-4 6 4"/></svg></div>
    <h3>ACQUISITIONS LAW</h3>
    <p style="width:215px">Guiding You Through Complex Transactions Complex Transactions</p>
    <a class="more" href="#">Learn More</a>
  </div>
</section>

<section class="team">
  <div class="abs center eyebrow" style="top:64px;font-size:17px">Meet Your Team</div>
  <h2 class="abs center section-title" style="top:91px">OUR ATTORENY</h2>

  <div class="member-photo photo" style="left:60px" role="img" aria-label="Portrait of attorney in a navy suit"></div>
  <div class="name-box" style="left:100px"><h4>Daniel Whitcombe</h4><span>CIVIL LAWYER</span><div class="social"></div></div>

  <div class="member-photo photo" style="left:427px" role="img" aria-label="Portrait of attorney in an office"></div>
  <div class="name-box" style="left:467px"><h4>Mei Lin Harper</h4><span>CIVIL LAWYER</span><div class="social"></div></div>

  <div class="member-photo photo" style="left:795px" role="img" aria-label="Portrait of attorney in a grey suit"></div>
  <div class="name-box" style="left:835px"><h4>Daniel Whitcombe</h4><span>CIVIL LAWYER</span><div class="social"></div></div>
</section>

<section class="testimonials">
  <h2 class="abs center" style="top:52px">WHAT OUR CLIENTS SAY</h2>
  <svg class="abs" style="left:578px;top:126px" width="44" height="34" viewBox="0 0 44 34" fill="#fff"><circle cx="10" cy="12" r="9"/><path d="M2 14c0 10 6 17 14 19l1-3c-6-3-8-8-8-12z"/><circle cx="32" cy="12" r="9"/><path d="M24 14c0 10 6 17 14 19l1-3c-6-3-8-8-8-12z"/></svg>
  <blockquote>Quis autem vel eum iure reprehenderit qui in ea voluptate velit esse quam nihil rentoa molestiae conseruatur vela illum qui dolorem eum fugiat ruo voluetas nulla ariatur minima veniam.Quis autem vel eum iure reprehenderit qui in ea voluptate velit esse quam nihil rentoa molestiae conseruatur vela illum qui dolorem eum fugiat ruo voluetas nulla ariatur minima veniam.</blockquote>
  <div class="abs center" style="top:320px;font-size:16px;font-weight:500">Oliver Brandt</div>
  <div class="abs center" style="top:344px;font-size:11px">KBR LEGAL</div>
  <div class="dots"><i class="on"></i><i></i><i></i><i></i></div>
</section>

<section class="blog">
  <div class="abs center eyebrow" style="top:80px;font-size:17px">Blogs</div>
  <h2 class="abs center section-title" style="top:106px;font-weight:600">News Feeds</h2>

  <article class="post" style="left:60px">
    <div class="thumb" role="img" aria-label="Hands signing a contract at a desk"></div>
    <div class="date">05<br>jun</div>
    <h4>Lorem ipsum dolor sit amet.</h4>
    <p>Lorem Ipsum has been the industry's standard dummy text ever since the 1500s, when an unknown printer took a galley...</p>
    <a class="btn" href="#">Learn More</a>
  </article>
  <article class="post" style="left:427px">
    <div class="thumb" role="img" aria-label="Lawyer speaking at a meeting table"></div>
    <div class="date">05<br>jun</div>
    <h4>Lorem ipsum dolor sit amet.</h4>
    <p>Lorem Ipsum has been the industry's standard dummy text ever since the 1500s, when an unknown printer took a galley...</p>
    <a class="btn" href="#">Learn More</a>
  </article>
  <article class="post" style="left:795px">
    <div class="thumb" role="img" aria-label="Agreement being signed over a table"></div>
    <div class="date">05<br>jun</div>
    <h4>Lorem ipsum dolor sit amet.</h4>
    <p>Lorem Ipsum has been the industry's standard dummy text ever since the 1500s, when an unknown printer took a galley...</p>
    <a class="btn" href="#">Learn More</a>
  </article>
</section>

<section class="contact">
  <div class="map" role="img" aria-label="Street map showing the office location"></div>
  <div class="contact-panel">
    <h2>Contact Us</h2>
    <div class="info" style="top:103px"><svg width="16" height="16" viewBox="0 0 24 24" fill="#17467c"><path d="M6.6 10.8a15 15 0 006.6 6.6l2.2-2.2c.3-.3.7-.4 1-.2 1.1.4 2.3.6 3.6.6.6 0 1 .4 1 1V20c0 .6-.4 1-1 1A17 17 0 013 4c0-.6.4-1 1-1h3.5c.6 0 1 .4 1 1 0 1.3.2 2.5.6 3.6.1.3 0 .7-.2 1z"/></svg>2750 Harbor Lane, Eastbrook, New Mexico 31190</div>
    <div class="info" style="top:131px"><svg width="16" height="14" viewBox="0 0 24 20" fill="#17467c"><path d="M2 2h20v16H2z" fill="none" stroke="#17467c" stroke-width="2"/><path d="M2 3l10 8 10-8z"/></svg>info@kbrlegal.com</div>
    <div class="info" style="top:159px"><svg width="16" height="18" viewBox="0 0 24 28" fill="#17467c"><path d="M12 0a10 10 0 00-10 10c0 8 10 18 10 18s10-10 10-18A10 10 0 0012 0zm0 14a4 4 0 110-8 4 4 0 010 8z"/></svg>100- Lorem ipsum simple text print</div>
    <div class="field" style="left:38px;top:223px;width:210px">Full Name</div>
    <div class="field" style="left:272px;top:223px;width:215px">Phone No</div>
    <div class="field" style="left:38px;top:266px;width:449px">Email Address</div>
    <div class="field" style="left:38px;top:309px;width:449px;padding-bottom:46px">Message</div>
    <a class="btn abs" href="#" style="left:36px;top:367px;width:128px;height:35px;font-size:13px">SUBMIT NOW</a>
  </div>
</section>

<footer class="footer">
  <div class="brand abs" style="left:60px;top:40px">KBR LEGAL</div>
  <div class="abs" style="left:60px;top:96px;display:flex;gap:8px"><div class="circle"></div><div class="circle"></div><div class="circle"></div></div>

  <div class="abs" style="left:282px;top:42px"><h4>COMPANY</h4><ul><li>Home</li><li>About us</li><li>Services</li><li>Team</li><li>Testimonials</li><li>Blog/Resources</li><li>Contact us</li></ul></div>
  <div class="abs" style="left:502px;top:42px"><h4>SERVICES</h4><ul><li>Commercial Law</li><li>Acquisitions Law</li><li>Property Law</li><li>Estates Law</li><li>Acquisition Law</li></ul></div>
  <div class="abs" style="left:718px;top:42px;width:210px">
    <h4>CONTACT US</h4>
    <div style="display:flex;gap:12px;font-size:12.5px;line-height:20px"><svg width="16" height="20" viewBox="0 0 24 28" fill="#fff" style="flex:none;margin-top:2px"><path d="M12 0a10 10 0 00-10 10c0 8 10 18 10 18s10-10 10-18A10 10 0 0012 0zm0 14a4 4 0 110-8 4 4 0 010 8z"/></svg><span>2750 Harbor Lane, Eastbrook, New Mexico 31190</span></div>
    <div style="display:flex;gap:12px;font-size:12.5px;margin-top:14px;align-items:center"><svg width="18" height="14" viewBox="0 0 24 20"><path d="M2 2h20v16H2z" fill="none" stroke="#fff" stroke-width="2"/><path d="M2 3l10 8 10-8z" fill="#fff"/></svg>info@kbrlegal.com</div>
    <div style="display:flex;gap:12px;font-size:12.5px;margin-top:16px;align-items:center"><svg width="16" height="16" viewBox="0 0 24 24" fill="#fff"><path d="M6.6 10.8a15 15 0 006.6 6.6l2.2-2.2c.3-.3.7-.4 1-.2 1.1.4 2.3.6 3.6.6.6 0 1 .4 1 1V20c0 .6-.4 1-1 1A17 17 0 013 4c0-.6.4-1 1-1h3.5c.6 0 1 .4 1 1 0 1.3.2 2.5.6 3.6.1.3 0 .7-.2 1z"/></svg>123 555 0190</div>
  </div>
  <div class="abs" style="left:944px;top:44px">
    <h4>NEWSLETTER</h4>
    <div style="width:197px;height:40px;background:#fff;border-radius:3px;color:#555;font-size:12px;padding:12px 14px">Your Email</div>
    <div style="margin-top:12px;width:128px;height:40px;border:1.5px solid #fff;border-radius:3px;display:flex;align-items:center;justify-content:center;font-size:14px">SUBSCRIBE</div>
  </div>
  <div class="abs" style="left:50px;top:282px;width:1100px;border-top:1px solid rgba(255,255,255,.25)"></div>
  <div class="abs center" style="top:302px;font-size:11px">©2025 KBR LEGAL PTY LTD - All rights reserved.</div>
</footer>

</body>
</html>
```